Business Consulting Business Card

professional business card with basic information (1) First and Last name (2) email address, (3) phone number, (4) website.

```html
<!DOCTYPE html>
<html lang="en">
<head>
<meta charset="utf-8">
<title>Bay Crest Capital – Business Card</title>
<link href="https://fonts.googleapis.com/css2?family=Poppins:wght@300;400;500&display=swap" rel="stylesheet">
<style>
  :root {
    --page-bg: #d8d3cc;
    --panel-dark: #1c2a33;
    --panel-deep: #0f171d;
    --frost-light: #eef0f0;
    --frost-mid: #d6dadb;
    --teal: #2f8a86;
    --teal-soft: #4fa7a1;
    --ink: #121a1f;
    --text-light: #e6ebee;
  }
  html, body {
    margin: 0;
    padding: 0;
    width: 1200px;
    height: 970px;
    overflow: hidden;
    background: var(--page-bg);
    font-family: "Poppins", sans-serif;
  }
  .canvas {
    position: relative;
    width: 1200px;
    height: 970px;
  }
  .business-card {
    position: absolute;
    left: 100px;
    top: 200px;
    width: 1000px;
    height: 569px;
    filter: drop-shadow(0 18px 30px rgba(0,0,0,0.22));
  }
  .card-text { font-family: "Poppins", sans-serif; }
  .holder-name { font-weight: 400; font-size: 35px; fill: var(--text-light); }
  .holder-role { font-weight: 300; font-size: 25px; fill: var(--teal-soft); }
  .address-line { font-weight: 300; font-size: 25px; fill: var(--text-light); }
  .contact-line { font-weight: 300; font-size: 26px; fill: var(--text-light); }
  .company-name { font-weight: 400; font-size: 50px; letter-spacing: 8px; fill: var(--ink); }
  .company-sub { font-weight: 400; font-size: 22px; letter-spacing: 26px; fill: var(--ink); }
  .icon-ring { fill: none; stroke: var(--teal); stroke-width: 2; }
  .icon-glyph { fill: none; stroke: var(--teal-soft); stroke-width: 2; stroke-linecap: round; stroke-linejoin: round; }
</style>
</head>
<body>
<main class="canvas">
  <svg class="business-card" viewBox="0 0 1040 592" xmlns="http://www.w3.org/2000/svg">
    <defs>
      <clipPath id="card-shape">
        <rect x="0" y="0" width="1040" height="592" rx="26" ry="26"/>
      </clipPath>
      <linearGradient id="frost-fill" x1="0" y1="0" x2="1" y2="1">
        <stop offset="0" stop-color="var(--frost-light)"/>
        <stop offset="0.6" stop-color="#e2e5e6"/>
        <stop offset="1" stop-color="var(--frost-mid)"/>
      </linearGradient>
      <radialGradient id="dark-fill" cx="0.35" cy="0.7" r="0.9">
        <stop offset="0" stop-color="#27363f"/>
        <stop offset="0.6" stop-color="var(--panel-dark)"/>
        <stop offset="1" stop-color="var(--panel-deep)"/>
      </radialGradient>
    </defs>

    <g clip-path="url(#card-shape)">
      <rect class="frost-side" x="0" y="0" width="1040" height="592" fill="url(#frost-fill)"/>
      <path class="dark-side" d="M0 0 H545 Q420 296 540 592 H0 Z" fill="url(#dark-fill)"/>
      <path class="edge-accent" d="M545 0 Q420 296 540 592" fill="none" stroke="var(--teal)" stroke-width="5"/>
      <path class="edge-accent-fine" d="M553 0 Q432 296 548 592" fill="none" stroke="#b9c2c4" stroke-width="2"/>
      <circle class="name-marker" cx="0" cy="150" r="28" fill="var(--teal)"/>
    </g>

    <g class="card-text">
      <text class="holder-name" x="68" y="153">OWEN HARTLEY</text>
      <text class="holder-role" x="68" y="180">Manager</text>

      <text class="address-line" x="67" y="289">PO BOX 480, Harbor Street</text>
      <text class="address-line" x="67" y="322">3rd Lane, Arizona 85004</text>

      <g class="contact-phone">
        <circle class="icon-ring" cx="80" cy="383" r="13"/>
        <path class="icon-glyph" d="M75 376 q-2 8 9 15 l3-3 -4-3 -2 2 q-4-3-5-7 l2-1 -1-4 z"/>
        <text class="contact-line" x="108" y="392">555.018.4726</text>
      </g>
      <g class="contact-email">
        <circle class="icon-ring" cx="80" cy="417" r="13"/>
        <rect class="icon-glyph" x="73" y="412" width="14" height="10" rx="1"/>
        <path class="icon-glyph" d="M73 412 l7 6 7-6"/>
        <text class="contact-line" x="108" y="425">owen@baycrestcap.com</text>
      </g>
      <g class="contact-web">
        <circle class="icon-ring" cx="80" cy="451" r="13"/>
        <circle class="icon-glyph" cx="80" cy="451" r="7"/>
        <path class="icon-glyph" d="M73 451 h14 M80 444 q-4 7 0 14 M80 444 q4 7 0 14"/>
        <text class="contact-line" x="108" y="460">www.baycrestcap.com</text>
      </g>

      <g class="company-block">
        <circle class="company-dot" cx="770" cy="230" r="32" fill="var(--teal)"/>
        <text class="company-name" x="774" y="344" text-anchor="middle">BAY CREST</text>
        <text class="company-sub" x="783" y="386" text-anchor="middle">CAPITAL</text>
      </g>
    </g>
  </svg>
</main>
</body>
</html>
```